Trade Show Backdrop

I need a fun and unique design using our colors and verbiage. I have uploaded an example of what was already created and as you can see, it's lame.
I need it to say the same thing, but I want a bit more flare to the layout and graphics.
I have also uploaded what the competition uses.
I would like a clean look, no pictures. Obviously it has to be scale for a 10x10 booth, stand and

Target Market(s)

Private, Commercial and Public

Font styles to use
Sans Serif

Colors
fbed22
ffffff

Requirements
Must have
• Yellow, Gray, Black & WhiteAsphalt background- uploaded

```html
<!DOCTYPE html>
<html lang="en">
<head>
<meta charset="utf-8">
<title>Pavement Solutions – Trade Show Backdrop</title>
<link href="https://fonts.googleapis.com/css2?family=Nunito:wght@800;900&family=Open+Sans:wght@300;600&display=swap" rel="stylesheet">
<style>
  :root {
    --sky-grey: #dcdde0;
    --brand-yellow: #f7cd1b;
    --sign-yellow: #fbed22;
    --ink: #111111;
    --white: #ffffff;
    --panel: rgba(22, 20, 20, 0.86);
  }
  html, body {
    margin: 0;
    padding: 0;
    overflow: hidden;
  }
  .backdrop {
    position: relative;
    width: 1200px;
    height: 1020px;
    overflow: hidden;
    background: var(--sky-grey);
    font-family: "Open Sans", sans-serif;
    color: var(--ink);
  }
  .road-scene {
    position: absolute;
    inset: 0;
  }
  .web-tab {
    position: absolute;
    left: 808px;
    top: 0;
    width: 327px;
    height: 58px;
    background: var(--brand-yellow);
    display: flex;
    align-items: center;
    justify-content: center;
    font-family: "Nunito", sans-serif;
    font-weight: 900;
    font-size: 25px;
    color: var(--ink);
  }
  .social-dots {
    position: absolute;
    left: 909px;
    top: 73px;
    display: flex;
    gap: 20px;
  }
  .social-dots span {
    width: 26px;
    height: 26px;
    border-radius: 50%;
    background: var(--ink);
  }
  .headline {
    position: absolute;
    left: 92px;
    top: 72px;
    margin: 0;
    line-height: 1;
  }
  .headline-light {
    display: block;
    font-weight: 300;
    font-size: 74px;
    letter-spacing: -1px;
  }
  .headline-bold {
    display: block;
    margin-top: 16px;
    font-family: "Nunito", sans-serif;
    font-weight: 900;
    font-size: 52px;
  }
  .brand-name {
    position: absolute;
    left: 822px;
    top: 226px;
    width: 300px;
    text-align: center;
    font-family: "Nunito", sans-serif;
    font-weight: 900;
    font-size: 48px;
    line-height: 48px;
    color: var(--ink);
  }
  .brand-mark {
    display: block;
    width: 16px;
    height: 16px;
    margin: 0 auto 14px;
    background: var(--ink);
  }
  .services-panel {
    position: absolute;
    left: 751px;
    top: 408px;
    width: 449px;
    height: 549px;
    border-top: 15px solid var(--brand-yellow);
    box-sizing: border-box;
    background: var(--panel);
    color: var(--white);
  }
  .section-title {
    margin: 0;
    font-family: "Nunito", sans-serif;
    font-weight: 900;
    font-size: 48px;
    line-height: 1;
  }
  .services-panel .section-title {
    position: absolute;
    left: 83px;
    top: 50px;
  }
  .item-list {
    list-style: none;
    margin: 0;
    padding: 0;
  }
  .item-list li {
    position: relative;
    height: 53px;
    font-weight: 600;
    font-size: 30px;
    line-height: 53px;
  }
  .item-list li::before {
    content: "";
    position: absolute;
    left: -29px;
    top: 21px;
    width: 12px;
    height: 12px;
    transform: rotate(45deg);
    background: currentColor;
  }
  .services-panel .item-list {
    position: absolute;
    left: 83px;
    top: 118px;
  }
  .services-panel .item-list li::before {
    background: var(--sign-yellow);
  }
  .solutions {
    position: absolute;
    left: 104px;
    top: 676px;
  }
  .solutions .item-list {
    margin-top: 10px;
  }
</style>
</head>
<body>
<main class="backdrop">
  <svg class="road-scene" width="1200" height="1020" viewBox="0 0 1200 1020">
    <defs>
      <linearGradient id="asphalt" x1="0" y1="0" x2="1" y2="0.4">
        <stop offset="0" stop-color="#232323"/>
        <stop offset="0.5" stop-color="#4a4a4c"/>
        <stop offset="1" stop-color="#2c2c2e"/>
      </linearGradient>
    </defs>
    <polygon points="0,1020 0,510 1200,924 1200,1020" fill="#f7cd1b"/>
    <polygon role="img" aria-label="Isometric road scene with a loader, crosswalk, curbs and road crew patching asphalt"
             points="0,288 1200,678 1200,924 0,510" fill="url(#asphalt)"/>
  </svg>

  <div class="web-tab">www.RoadMaven.com</div>
  <div class="social-dots" aria-label="Social media links">
    <span></span><span></span><span></span>
  </div>

  <h1 class="headline">
    <span class="headline-light">Pavement Solutions</span>
    <span class="headline-bold">Custom Made for You</span>
  </h1>

  <div class="brand-name"><span class="brand-mark"></span>The<br>Road<br>Maven</div>

  <section class="services-panel">
    <h2 class="section-title">Services</h2>
    <ul class="item-list">
      <li>Asphalt Paving</li>
      <li>Asphalt Milling</li>
      <li>Sealcoating</li>
      <li>Pavement Repair</li>
      <li>Concrete Sidewalks</li>
      <li>Concrete Curbs</li>
      <li>Pavement Markings</li>
      <li>Signage</li>
    </ul>
  </section>

  <section class="solutions">
    <h2 class="section-title">Solutions</h2>
    <ul class="item-list">
      <li>Professionally Managed</li>
      <li>ADA Compliance</li>
      <li>Site Evaluation</li>
      <li>Project &amp; Asset Management</li>
    </ul>
  </section>
</main>
</body>
</html>
```